Every Drawer Neatly Sorted or EDN Organized needs a business card design. EDN Organized is a professi

We need a business card design that is clean, sharp and conveys a sense of organization. I already have a logo.

Target Market(s)

Families (specifically mothers), small business owners, parents, seniors

Industry/Entity Type

Business

Contact Information for Business Card

My website is www.ednorganized-example.com and my Facebook page is http://www.socialpage-example.com/everydrawerneatlysorted. The phone number is 555-418-2706 and I want to be listed as Miriel O. Dunsford, Owner

Requirements
Must have
• My logo.

```html
<!DOCTYPE html>
<html lang="en">
<head>
<meta charset="utf-8">
<title>EDN Organized – Business Card</title>
<link rel="stylesheet" href="https://fonts.googleapis.com/css2?family=Open+Sans:wght@400;600&display=swap">
<style>
  :root {
    --backdrop: #e9e9e7;
    --card: #ffffff;
    --brand-blue: #1a7fd6;
    --ink: #2b2b2b;
    --dark-panel: #000000;
    --rule: #5aa0dd;
  }
  * { margin: 0; padding: 0; box-sizing: border-box; }
  html, body {
    width: 1200px; height: 900px; overflow: hidden;
    background: var(--backdrop);
    font-family: "Open Sans", Arial, sans-serif;
  }
  .canvas { position: relative; width: 1200px; height: 900px; }
  .card {
    position: absolute; background: var(--card);
    box-shadow: 0 6px 18px rgba(0,0,0,.18);
    overflow: hidden;
  }
  .card-front { left: 238px; top: 60px; width: 555px; height: 345px; }
  .front-panel { position: absolute; inset: 0; }
  .front-brand {
    position: absolute; left: 60px; top: 110px;
    display: flex; align-items: center; gap: 18px;
    color: var(--brand-blue); font-weight: 400; font-size: 72px; letter-spacing: 4px;
  }
  .front-brand .mark-dot {
    width: 34px; height: 34px; border-radius: 50%; background: var(--brand-blue);
  }
  .card-back { left: 457px; top: 518px; width: 560px; height: 343px; }
  .back-brand {
    position: absolute; left: 0; right: 0; top: 80px; text-align: center;
    color: var(--brand-blue); font-weight: 400; font-size: 25px; letter-spacing: 2px;
  }
  .person {
    position: absolute; right: 304px; top: 193px; text-align: right;
  }
  .person-name { color: var(--brand-blue); font-weight: 600; font-size: 17px; }
  .person-role { color: var(--ink); font-size: 14px; margin-top: 1px; }
  .contact-list {
    position: absolute; left: 280px; top: 183px; list-style: none;
    color: var(--ink); font-size: 14.5px; line-height: 20px;
  }
  .contact-list li { display: flex; align-items: center; gap: 8px; white-space: nowrap; }
  .contact-list svg { width: 12px; height: 12px; fill: var(--brand-blue); flex: none; }
  .social-row {
    position: absolute; left: 0; right: 0; top: 271px;
    display: flex; align-items: center; gap: 8px;
  }
  .social-row .rule { flex: 1; height: 1px; background: var(--rule); }
  .social-link { color: var(--brand-blue); font-size: 14px; white-space: nowrap; }
</style>
</head>
<body>
<main class="canvas">
  <section class="card card-front">
    <svg class="front-panel" viewBox="0 0 555 345" aria-hidden="true">
      <polygon points="497,0 555,0 555,345 162,345" fill="var(--dark-panel)"/>
    </svg>
    <div class="front-brand"><span class="mark-dot"></span><span>EDN</span></div>
  </section>

  <section class="card card-back">
    <div class="back-brand">Every Drawer Neatly Sorted</div>

    <div class="person">
      <div class="person-name">Miriel O. Dunsford</div>
      <div class="person-role">Owner</div>
    </div>

    <ul class="contact-list">
      <li><svg viewBox="0 0 24 24"><path d="M6.6 10.8a15.1 15.1 0 0 0 6.6 6.6l2.2-2.2a1 1 0 0 1 1-.25 11.4 11.4 0 0 0 3.6.57 1 1 0 0 1 1 1V20a1 1 0 0 1-1 1A17 17 0 0 1 3 4a1 1 0 0 1 1-1h3.5a1 1 0 0 1 1 1c0 1.25.2 2.45.57 3.57a1 1 0 0 1-.25 1z"/></svg>555-418-2706</li>
      <li><svg viewBox="0 0 24 24"><path d="M2 5h20v14H2z M2 5l10 8 10-8" stroke="#fff" stroke-width="1.6"/></svg>info@ednorganized.com</li>
      <li><svg viewBox="0 0 24 24"><circle cx="12" cy="12" r="10"/><path d="M2 12h20M12 2c3 3 3 17 0 20M12 2c-3 3-3 17 0 20" stroke="#fff" stroke-width="1.4" fill="none"/></svg>www.ednorganized-example.com</li>
    </ul>

    <div class="social-row">
      <span class="rule"></span>
      <span class="social-link">www.socialpage-example.com/everydrawerneatlysorted</span>
      <span class="rule"></span>
    </div>
  </section>
</main>
</body>
</html>
```